Clean business card with logo provided

I want a card that will stand out among the masses. I need the color and image to show professionalism and yet have a family appeal showing that I only deal with win/win scenarios. The back of the card will be used to take notes about the individual so I can use that in my database entry. I like modern design but need professionalism in it also. It needs to fit my "clean, safe, and affordable housing" motto. I need to be able to write on the file and update the card details for my employees.

Target Market(s)

Investors looking to make investment income through real estate

Industry/Entity Type

Real Estate

Contact Information for Business Card

Troy Vandemark
blank address, city, st, zip code
480-555-0147
troyvandemark@quillrentals.example
www.quillrentals.example

Font styles to use
Sans Serif

Requirements
Must have
• I would like the back of the card to have lines for info. example
• Met/Visited: Date:
• Interets:
Nice to have
• I want the cards color to match the logo background color. Font with details to be san serif and black. I want the card rectangular with square corners. Standard business card size. I would like to see cards designed with both images to see which i prefer more.

```html
<!DOCTYPE html>
<html lang="en">
<head>
<meta charset="utf-8">
<title>Quill Rentals LLC – Business Card</title>
<link href="https://fonts.googleapis.com/css2?family=Cinzel:wght@400;500&family=Open+Sans:ital,wght@0,400;0,600;1,400&display=swap" rel="stylesheet">
<style>
  :root {
    --teal: #0f9fb8;
    --teal-deep: #0a8aa1;
    --ink: #050505;
    --paper: #e9eaec;
    --rule: #1c1c1c;
    --silver: #dfe3e6;
    --backdrop: #f3f4f5;
  }
  * { margin: 0; padding: 0; box-sizing: border-box; }
  html, body { width: 1105px; height: 1200px; overflow: hidden; background: var(--backdrop); }
  body { position: relative; font-family: "Open Sans", Arial, sans-serif; }

  .card { position: absolute; left: 178px; width: 750px; height: 428px; overflow: hidden; }
  .card--front { top: 118px; background: var(--ink); }
  .card--back { top: 640px; background: var(--paper); }

  .brand { position: absolute; display: flex; flex-direction: column; align-items: center; }
  .brand__row { display: flex; align-items: center; gap: 16px; }
  .brand__name {
    font-family: "Cinzel", Georgia, serif; font-weight: 500; font-size: 36px;
    letter-spacing: 3px; white-space: nowrap; line-height: 1;
  }
  .brand__dot { width: 26px; height: 26px; border-radius: 50%; }
  .brand__tagline { margin-top: 10px; font-size: 12px; font-weight: 600; letter-spacing: .2px; }

  .card--front .brand { right: 44px; top: 48px; }
  .card--front .brand__name { color: var(--teal); }
  .card--front .brand__dot { background: var(--silver); }
  .card--front .brand__tagline { color: var(--teal); }

  .holder { position: absolute; left: 42px; top: 250px; width: 661px; }
  .holder__name {
    font-family: "Cinzel", Georgia, serif; font-weight: 400; font-size: 29px; color: var(--teal);
    letter-spacing: .5px; padding-bottom: 10px; border-bottom: 1px solid #8a8a8a;
  }
  .contact { display: flex; justify-content: space-between; margin-top: 14px; color: #f2f2f2; font-size: 20px; line-height: 28px; }
  .contact__item { display: flex; align-items: center; gap: 12px; }
  .contact__item svg { width: 16px; height: 16px; fill: var(--teal); flex: none; }
  .contact__address { text-align: right; }

  .footer-band { position: absolute; left: 0; bottom: 0; width: 750px; height: 38px; }
  .footer-band__url {
    position: absolute; right: 42px; bottom: 4px; color: var(--ink);
    font-size: 21px; font-style: italic; letter-spacing: 1px;
  }

  .back-header { position: absolute; left: 0; top: 0; width: 750px; height: 212px; background: var(--teal); }
  .card--back .brand { left: 0; right: 0; top: 62px; }
  .card--back .brand__name { color: #ffffff; }
  .card--back .brand__dot { background: var(--ink); }
  .card--back .brand__tagline { color: #f4fbfc; }

  .notes { position: absolute; left: 57px; top: 262px; width: 636px; color: var(--teal); font-size: 19px; }
  .notes__row { display: flex; align-items: flex-end; height: 30px; margin-bottom: 22px; }
  .notes__label { white-space: nowrap; margin-right: 6px; }
  .notes__line { flex: 1; border-bottom: 1.5px solid var(--rule); height: 22px; }
  .notes__line--met { flex: 0 0 256px; }
  .notes__label--date { margin-left: 10px; }
  .notes__line--blank { margin-left: 6px; }
</style>
</head>
<body>

<section class="card card--front" aria-label="Business card front">
  <div class="brand">
    <div class="brand__row">
      <span class="brand__name">QUILL RENTALS LLC</span>
      <span class="brand__dot"></span>
    </div>
    <p class="brand__tagline">Well kept homes at fair and honest rents</p>
  </div>

  <div class="holder">
    <h1 class="holder__name">TROY VANDEMARK</h1>
    <div class="contact">
      <div class="contact__list">
        <div class="contact__item">
          <svg viewBox="0 0 24 24" aria-hidden="true"><path d="M6.6 10.8a15.2 15.2 0 0 0 6.6 6.6l2.2-2.2c.3-.3.7-.4 1-.2 1.1.4 2.3.6 3.6.6.6 0 1 .4 1 1V20c0 .6-.4 1-1 1A17 17 0 0 1 3 4c0-.6.4-1 1-1h3.5c.6 0 1 .4 1 1 0 1.3.2 2.5.6 3.6.1.3 0 .7-.2 1z"/></svg>
          <span>480-555-0147</span>
        </div>
        <div class="contact__item">
          <svg viewBox="0 0 24 24" aria-hidden="true"><path d="M2 5h20v2l-10 6L2 7zM2 9l10 6 10-6v10H2z"/></svg>
          <span>troyvandemark@quillrentals.example</span>
        </div>
      </div>
      <div class="contact__address">
        <div>2318 Juniper Court</div>
        <div>Anchorage, Alaska 99508</div>
      </div>
    </div>
  </div>

  <svg class="footer-band" viewBox="0 0 750 38" aria-hidden="true">
    <polygon points="0,14 430,14 422,24 0,24" fill="#f2f2f2"/>
    <polygon points="0,28 750,28 750,38 0,38" fill="var(--teal-deep)"/>
    <polygon points="440,2 750,2 750,38 410,38" fill="var(--teal)"/>
  </svg>
  <span class="footer-band__url">quillrentals.example</span>
</section>

<section class="card card--back" aria-label="Business card back">
  <div class="back-header"></div>
  <div class="brand">
    <div class="brand__row">
      <span class="brand__name">QUILL RENTALS LLC</span>
      <span class="brand__dot"></span>
    </div>
    <p class="brand__tagline">Well kept homes at fair and honest rents</p>
  </div>

  <div class="notes">
    <div class="notes__row">
      <span class="notes__label">MET/VISITED:</span>
      <span class="notes__line notes__line--met"></span>
      <span class="notes__label notes__label--date">DATE:</span>
      <span class="notes__line"></span>
    </div>
    <div class="notes__row">
      <span class="notes__label">INTERETS:</span>
      <span class="notes__line"></span>
    </div>
    <div class="notes__row">
      <span class="notes__line notes__line--blank"></span>
    </div>
  </div>
</section>

</body>
</html>
```